Roaming outings business card

please see website
www.roamingoutings.comau

info needed on card
Keiran Voss
Ph
email
Adventure Riding GPS trails

please use my logo and colours off my site

Business

Keiran Voss
keiran@roamingoutings.com

```html
<!DOCTYPE html>
<html lang="en">
<head>
<meta charset="utf-8">
<title>Roaming Outings – Business Card</title>
<link href="https://fonts.googleapis.com/css2?family=Open+Sans:wght@400;600;800&display=swap" rel="stylesheet">
<style>
  :root {
    --canvas-bg: #e8e5e0;
    --card-bg: #ffffff;
    --ink: #1b1b1b;
    --brand-yellow: #f2c200;
    --pattern-grey: #dcdcdc;
    --pattern-yellow: #f7ecb8;
    --mark-grey: #6f6f6f;
  }
  * { box-sizing: border-box; margin: 0; padding: 0; }
  html, body {
    width: 1200px; height: 900px; overflow: hidden;
    background: var(--canvas-bg);
    font-family: "Open Sans", Arial, sans-serif;
    color: var(--ink);
  }
  .canvas { position: relative; width: 1200px; height: 900px; }
  .card {
    position: absolute; left: 270px; width: 660px; height: 377px;
    background: var(--card-bg);
    box-shadow: 0 6px 18px rgba(0,0,0,.18);
    overflow: hidden;
  }
  .card--back { top: 48px; }
  .card--front { top: 475px; }

  .back-pattern {
    position: absolute; inset: 0;
    background:
      radial-gradient(circle at 30% 35%, var(--pattern-yellow) 0 8%, transparent 9%),
      radial-gradient(circle at 65% 20%, var(--pattern-yellow) 0 7%, transparent 8%),
      linear-gradient(135deg, var(--pattern-grey) 0%, #f1f1f1 55%, #ffffff 80%);
  }
  .back-name {
    position: absolute; right: 34px; bottom: 70px;
    font-weight: 800; font-size: 46px; line-height: 1.02;
    text-transform: uppercase; text-align: left; letter-spacing: 1px;
    color: var(--ink);
  }

  .brand { position: absolute; left: 50px; top: 40px; display: flex; align-items: center; gap: 16px; }
  .brand-dot { width: 70px; height: 70px; border-radius: 50%; background: var(--brand-yellow); flex: none; }
  .brand-name {
    font-weight: 800; font-size: 27px; line-height: 1.02; text-transform: uppercase; color: var(--ink);
  }
  .tagline {
    position: absolute; left: 60px; top: 130px;
    font-weight: 600; font-size: 19px; color: var(--ink);
  }
  .contact { position: absolute; left: 420px; top: 190px; }
  .contact-name { color: var(--brand-yellow); font-weight: 600; font-size: 19px; margin-bottom: 14px; }
  .contact-list { list-style: none; }
  .contact-item { display: flex; align-items: center; gap: 8px; font-size: 15px; margin-bottom: 6px; }
  .contact-icon {
    width: 18px; height: 18px; border-radius: 3px; background: var(--brand-yellow);
    display: flex; align-items: center; justify-content: center; flex: none;
  }
</style>
</head>
<body>
<main class="canvas">
  <section class="card card--back">
    <div class="back-pattern" role="img" aria-label="Repeating pattern of the brand symbol in soft grey and pale yellow"></div>
    <p class="back-name">Roaming<br>Outings</p>
  </section>

  <section class="card card--front">
    <div class="brand">
      <span class="brand-dot"></span>
      <p class="brand-name">Roaming<br>Outings</p>
    </div>
    <p class="tagline">Adventure Riding GPS trails</p>

    <div class="contact">
      <p class="contact-name">Keiran Voss</p>
      <ul class="contact-list">
        <li class="contact-item">
          <span class="contact-icon">
            <svg width="12" height="12" viewBox="0 0 12 12"><path d="M3 1l2 2-1 1.5a6 6 0 0 0 3.5 3.5L9 7l2 2-1.5 2A9 9 0 0 1 1 2.5z" fill="#1b1b1b"/></svg>
          </span>(044)-555-0192
        </li>
        <li class="contact-item">
          <span class="contact-icon">
            <svg width="12" height="10" viewBox="0 0 12 10"><rect x="0.5" y="1" width="11" height="8" fill="#1b1b1b"/><path d="M1 1.5l5 4 5-4" stroke="#f2c200" fill="none"/></svg>
          </span>info@roamingoutings.com
        </li>
        <li class="contact-item">
          <span class="contact-icon">
            <svg width="12" height="12" viewBox="0 0 12 12"><path d="M5 7l2-2M4.5 5.5L3 7a2 2 0 0 0 2.8 2.8L7.3 8.3M7.5 6.5L9 5a2 2 0 0 0-2.8-2.8L4.7 3.7" stroke="#1b1b1b" stroke-width="1.4" fill="none" stroke-linecap="round"/></svg>
          </span>www.roamingoutings.com
        </li>
      </ul>
    </div>
  </section>
</main>
</body>
</html>
```